could someone please design some snazzy business cards for "Tidy Meadow"
the website is tidymeadow.co.nz

the logo is attached

name : Harriet Osbrook
Contact Number: 0224819357
email: harrietosb@tidymeadow.co.nz
Slogan: Competitive prices, and personal service in the Wanganui district

The theme is green as its for a lawn mowing outfit!

```html
<!DOCTYPE html>
<html lang="en">
<head>
<meta charset="utf-8">
<title>Tidy Meadow – Business Card</title>
<link rel="stylesheet" href="https://fonts.googleapis.com/css2?family=Poiret+One&family=Tinos:wght@700&display=swap">
<style>
  :root {
    --canvas-black: #000000;
    --card-charcoal: #3a3a3a;
    --card-meadow: #8fbc5e;
    --brand-olive: #5c6f12;
    --leaf-light: #a6cf72;
    --ink-dark: #2e2e2e;
    --tag-border: #cfcfcf;
  }
  * { margin: 0; padding: 0; box-sizing: border-box; }
  html, body {
    width: 1131px;
    height: 1200px;
    overflow: hidden;
    background: var(--canvas-black);
  }
  .canvas {
    position: relative;
    width: 1131px;
    height: 1200px;
  }
  .card {
    position: absolute;
    left: 114px;
    width: 930px;
    height: 497px;
  }
  .card--front { top: 62px; background: var(--card-charcoal); }
  .card--back  { top: 628px; background: var(--card-meadow); }

  .brand-dot {
    position: absolute;
    border-radius: 50%;
    background: var(--brand-olive);
  }
  .brand-name {
    position: absolute;
    font-family: "Tinos", "Times New Roman", serif;
    font-weight: 700;
    color: var(--brand-olive);
    white-space: nowrap;
    transform: translateX(-50%);
  }

  /* front */
  .card--front .brand-dot { width: 150px; height: 150px; left: 390px; top: 140px; }
  .card--front .brand-name { left: 465px; top: 355px; font-size: 37px; }
  .front-web {
    position: absolute;
    left: 465px;
    top: 440px;
    transform: translateX(-50%);
    font-family: "Poiret One", sans-serif;
    font-size: 31px;
    color: var(--leaf-light);
    white-space: nowrap;
  }

  /* back */
  .name-tag {
    position: absolute;
    left: 664px;
    top: 32px;
    width: 266px;
    height: 68px;
    background: var(--card-charcoal);
    border: 2px solid var(--tag-border);
    border-right: none;
    display: flex;
    align-items: center;
    justify-content: center;
    font-family: "Poiret One", sans-serif;
    font-size: 31px;
    color: var(--leaf-light);
    white-space: nowrap;
  }
  .card--back .brand-dot { width: 82px; height: 82px; left: 247px; top: 160px; }
  .card--back .brand-name { left: 288px; top: 295px; font-size: 24px; }

  .contact-list {
    position: absolute;
    left: 462px;
    top: 186px;
    list-style: none;
    font-family: "Poiret One", sans-serif;
    font-size: 21px;
    font-weight: 400;
    color: var(--ink-dark);
  }
  .contact-list li { height: 42px; display: flex; }
  .contact-list .label { width: 38px; }

  .slogan {
    position: absolute;
    left: 0;
    right: 0;
    top: 436px;
    text-align: center;
    font-family: "Poiret One", sans-serif;
    font-size: 28px;
    color: var(--ink-dark);
    white-space: nowrap;
  }
</style>
</head>
<body>
  <main class="canvas">
    <section class="card card--front">
      <span class="brand-dot"></span>
      <p class="brand-name">Tidy Meadow</p>
      <p class="front-web">www.tidymeadow.co.nz</p>
    </section>

    <section class="card card--back">
      <p class="name-tag">Harriet Osbrook</p>
      <span class="brand-dot"></span>
      <p class="brand-name">Tidy Meadow</p>
      <ul class="contact-list">
        <li><span class="label">T :</span><span>0224819357</span></li>
        <li><span class="label">E :</span><span>harrietosb@tidymeadow.co.nz</span></li>
        <li><span class="label">W :</span><span>www.tidymeadow.co.nz</span></li>
      </ul>
      <p class="slogan">Competitive prices, and personal service&nbsp; in the Wanganui district</p>
    </section>
  </main>
</body>
</html>
```